BRISK SWEEP

Need a professional looking business card that can fit : Name, Title, Cell, and office phone numbers. On the flip side we would like a list of our services : Highway accident management and towing, Crime scene clean up, Illegal drug lab clean up, Drug disposal, and Hazardous materials clean up.

```html
<!DOCTYPE html>
<html lang="en">
<head>
<meta charset="utf-8">
<title>Brisk Sweep — Business Card</title>
<link href="https://fonts.googleapis.com/css2?family=Cinzel:wght@400;600;700&display=swap" rel="stylesheet">
<style>
  :root {
    --navy: #1f3866;
    --gold: #e6b52c;
    --star-red: #c6202f;
    --paper: #f8f8f6;
    --backdrop: #e8e5e0;
    --faint: rgba(31, 56, 102, 0.08);
  }
  * { box-sizing: border-box; margin: 0; padding: 0; }
  html, body {
    width: 1200px; height: 1200px; overflow: hidden;
    background: var(--backdrop);
    font-family: "Cinzel", "Times New Roman", serif;
    color: var(--navy);
  }
  .sheet { position: relative; width: 1200px; height: 1200px; }
  .card {
    position: absolute; left: 150px; width: 900px; height: 514px;
    background: var(--paper);
    box-shadow: 0 6px 22px rgba(0,0,0,0.18);
  }
  .card--front { top: 56px; }
  .card--back { top: 630px; }

  /* Front */
  .brand-seal {
    position: absolute; left: 70px; top: 107px;
    width: 300px; height: 300px; border-radius: 50%;
    border: 10px solid var(--navy);
    display: flex; align-items: center; justify-content: center;
    text-align: center;
  }
  .brand-seal__name {
    font-weight: 700; font-size: 40px; line-height: 1.15; letter-spacing: 1px;
    color: var(--navy);
  }
  .identity { position: absolute; right: 60px; top: 92px; width: 420px; text-align: right; }
  .identity__name { font-weight: 700; font-size: 36px; letter-spacing: 0.5px; }
  .identity__title { font-size: 24px; color: var(--gold); margin-top: 2px; }
  .identity__rule { height: 2px; background: var(--gold); margin: 26px 0 24px; }
  .contact { list-style: none; }
  .contact__line {
    display: flex; justify-content: flex-end; align-items: center; gap: 12px;
    font-size: 28px; line-height: 1.35; font-family: "Cinzel", serif;
  }
  .contact__icon { width: 30px; height: 30px; fill: var(--navy); }
  .address { margin-top: 22px; font-size: 28px; line-height: 1.3; }

  /* Back */
  .watermark {
    position: absolute; left: 300px; top: 107px; width: 300px; height: 300px;
    border-radius: 50%; border: 10px solid var(--faint);
    display: flex; align-items: center; justify-content: center; text-align: center;
  }
  .watermark__name { font-weight: 700; font-size: 40px; line-height: 1.15; color: var(--faint); }
  .services {
    position: absolute; left: 62px; top: 172px; list-style: none;
  }
  .services__item {
    font-size: 29px; font-weight: 600; line-height: 1.3; letter-spacing: 0.3px;
    display: flex; align-items: baseline; gap: 6px;
  }
  .services__star { color: var(--star-red); font-size: 26px; font-family: serif; }
</style>
</head>
<body>
<main class="sheet">

  <section class="card card--front" aria-label="Business card front">
    <div class="brand-seal">
      <span class="brand-seal__name">BRISK<br>SWEEP</span>
    </div>

    <div class="identity">
      <h1 class="identity__name">Daniel R Hollis</h1>
      <p class="identity__title">Principal</p>
      <div class="identity__rule"></div>
      <ul class="contact">
        <li class="contact__line">
          <svg class="contact__icon" viewBox="0 0 24 24" aria-hidden="true"><rect x="7" y="2" width="10" height="20" rx="2"/><rect x="9" y="5" width="6" height="11" fill="#f8f8f6"/></svg>
          <span>(304) 555-0142</span>
        </li>
        <li class="contact__line">
          <svg class="contact__icon" viewBox="0 0 24 24" aria-hidden="true"><rect x="3" y="2" width="5" height="20" rx="1"/><rect x="9" y="5" width="12" height="17" rx="1"/><g fill="#f8f8f6"><rect x="11" y="7" width="8" height="3"/><rect x="11" y="12" width="2" height="2"/><rect x="14" y="12" width="2" height="2"/><rect x="17" y="12" width="2" height="2"/><rect x="11" y="16" width="2" height="2"/><rect x="14" y="16" width="2" height="2"/><rect x="17" y="16" width="2" height="2"/></g></svg>
          <span>(304) 555-0187</span>
        </li>
      </ul>
      <p class="address">2240 Ridge Hollow Road<br>Kanawha City, WV 25314</p>
    </div>
  </section>

  <section class="card card--back" aria-label="Business card back">
    <div class="watermark" aria-hidden="true">
      <span class="watermark__name">BRISK<br>SWEEP</span>
    </div>
    <ul class="services">
      <li class="services__item"><span class="services__star">★</span>Highway accident management and towing</li>
      <li class="services__item"><span class="services__star">★</span>Crime scene clean up</li>
      <li class="services__item"><span class="services__star">★</span>Illegal drug lab clean up</li>
      <li class="services__item"><span class="services__star">★</span>Drug disposal and</li>
      <li class="services__item"><span class="services__star">★</span>Hazardous materials clean up</li>
    </ul>
  </section>

</main>
</body>
</html>
```